Stationary Design for Quince consultant and support company

We need new stationary designed for a London based support company that provide on-site and remote support services for Quince products. Our clients are both consumers and businesses.

We would like a letterhead, compliment slip, business card and possibly an e-mail signature designed.

Business card designs can be either 1 side or 2, depending on designs we receive we may choose a preference for 1 or 2 sides later on in the design stage.

Designs needs to be at least 300dpi and should be done using CMYK colours.

We want the design to be bold, easy to read, clean and professional.

We have attached our company logo in 2 colour variations (if you need any other source files then please ask).

Our logo colours are as follows:

Blue (85, 50, 0, 0) and Green (50, 0, 100, 0)

We use two different suppliers for out stationary so here are the size dimensions for both. Unfortunately they are ever so slightly different size wise so hopefully we can get something that accommodates both, we can provide dimensions if required for final versions.

Some fonts that have been used before with our company are Probert (for tagline on our company logo) and previously had Nauman used, however we are very much open to seeing what the designers come up with and the fonts mentioned are not a requirement.
Updates

Company details for designs (however the template should be editable for multiple staff) Vorbin Ltd. Registered Office: 62-74 Harlow Lane London N7 2QD 020 7915 3381 www.vorbin.example info@vorbin.example Company is Registered in England and Wales Company No. 07351649 Directors details (if you want to make the template using his details), rest of the details are as above Dan Moss Director dan@vorbin.example

Hi all, Thank you for your submissions so far. Could we please ask that you don't use the logo with the tagline from our website for the stationary designs and only the logos provided in the design brief. For the business cards we are looking at normal rectangular business cards to be used and we can provide a template guide for size if needed, please just ask. Regards Vorbin Team

Target Market(s)

Our target market are consumers (of all ages) and small/medium businesses.

Industry/Entity Type

Business

Font styles to use
Serif
Sans Serif

Requirements
Must have
• At least business card, letterhead and compliment slip submitted (we need all 3 designed this time round)
Should not have
• Business cards should not have the writing "registered office" (letterheads and compliment slips can along the bottom edge)

```html
<!DOCTYPE html>
<html lang="en">
<head>
<meta charset="utf-8">
<title>Vorbin Business Card</title>
<link rel="stylesheet" href="https://fonts.googleapis.com/css2?family=Ubuntu:wght@300;400;500;700&display=swap">
<style>
  :root {
    --backdrop: #cfe0ee;
    --card: #fbfbfa;
    --blue: #3a86c4;
    --green: #8cc34d;
    --ink: #333638;
    --ink-soft: #55595c;
  }
  * { box-sizing: border-box; margin: 0; padding: 0; }
  html, body {
    width: 1200px; height: 1000px; overflow: hidden;
    background: var(--backdrop);
    font-family: "Ubuntu", sans-serif;
    color: var(--ink);
  }
  .card {
    position: absolute;
    width: 560px; height: 340px;
    background: var(--card);
    overflow: hidden;
    box-shadow: 0 2px 0 #2f3438, 0 8px 20px rgba(40, 70, 100, 0.18);
  }
  .card--front { left: 80px; top: 100px; }
  .card--back { left: 560px; top: 560px; }
  .card__shapes { position: absolute; inset: 0; }
  .wordmark {
    position: absolute;
    font-weight: 700;
    letter-spacing: 2px;
    color: var(--ink);
    text-transform: uppercase;
    white-space: nowrap;
  }
  .card--front .wordmark { left: 44px; top: 148px; font-size: 40px; }
  .card--back .wordmark { left: 90px; top: 150px; font-size: 28px; }
  .rule {
    position: absolute; height: 1.5px; background: var(--blue);
    left: 250px; right: 24px;
  }
  .rule--top { top: 112px; }
  .rule--bottom { top: 262px; }
  .person { position: absolute; left: 250px; top: 146px; }
  .person__name { font-size: 26px; font-weight: 500; color: var(--ink); line-height: 1.1; }
  .person__role { font-size: 20px; font-weight: 300; color: var(--ink-soft); line-height: 1.1; }
  .contact {
    position: absolute; font-size: 10.5px; color: var(--ink-soft);
    line-height: 1.45; display: flex; gap: 5px;
  }
  .contact svg { flex: none; margin-top: 2px; }
  .contact--phone { top: 122px; right: 28px; }
  .contact--address { top: 218px; left: 250px; }
  .contact--online { top: 218px; left: 400px; flex-direction: column; gap: 0; }
  .contact--online span { display: flex; gap: 5px; align-items: center; }
</style>
</head>
<body>

<section class="card card--front">
  <svg class="card__shapes" width="560" height="340" viewBox="0 0 560 340">
    <rect class="panel-blue" fill="var(--blue)" x="330" y="0" width="150" height="340"/>
    <rect class="strip-green" fill="var(--green)" x="510" y="0" width="50" height="340"/>
  </svg>
  <div class="wordmark">Vorbin</div>
</section>

<section class="card card--back">
  <svg class="card__shapes" width="560" height="340" viewBox="0 0 560 340">
    <polygon fill="var(--green)" points="0,0 100,0 0,140"/>
    <polygon fill="var(--green)" points="0,250 230,340 0,340"/>
  </svg>
  <div class="wordmark">Vorbin</div>
  <div class="rule rule--top"></div>
  <div class="contact contact--phone">
    <svg width="9" height="9" viewBox="0 0 10 10"><path fill="var(--blue)" d="M2 0.5l1.6 2-1 1.1a6 6 0 0 0 3.8 3.8l1.1-1 2 1.6-1 1.5C4.6 9.6 0.4 5.4 0.5 1.5z"/></svg>
    020 7915 3381
  </div>
  <div class="person">
    <div class="person__name">Dan Moss</div>
    <div class="person__role">Director</div>
  </div>
  <div class="contact contact--address">
    <svg width="8" height="11" viewBox="0 0 8 11"><path fill="var(--blue)" d="M4 0a4 4 0 0 1 4 4c0 3-4 7-4 7S0 7 0 4a4 4 0 0 1 4-4zm0 2.3a1.7 1.7 0 1 0 0 3.4 1.7 1.7 0 0 0 0-3.4z"/></svg>
    <div>62-74 Harlow Lane<br>London N7 2QD</div>
  </div>
  <div class="contact contact--online">
    <span><svg width="9" height="9" viewBox="0 0 10 10"><circle cx="5" cy="5" r="5" fill="var(--blue)"/></svg>www.vorbin.example</span>
    <span><svg width="10" height="8" viewBox="0 0 10 8"><rect width="10" height="8" rx="1" fill="var(--blue)"/><path d="M0.5 0.8l4.5 3.6 4.5-3.6" stroke="#fff" fill="none" stroke-width="0.9"/></svg>dan@vorbin.example</span>
  </div>
  <div class="rule rule--bottom"></div>
</section>

</body>
</html>
```